Business Card Design.

Life and Wellness Coach
www.brightpathwell.com
Want to use my name as the logo it could be the initials TRH or my full name. I want to trade mark me.
I like clean lines and simple designs, but it pops using the colors scheme (one or two colors) on the website.
I provide life and health coaching virtually and in person. My services include: Nutrition Response Testing, Allergy Elimination Testing, Wellness Coaching, Life Coaching. Life and Health Assessments, and I sell foundational health products and specialized nutrition. Use colors that represent healing and trust.
Target Market(s)
Women for the ages of 30 - 60
Industry/Entity Type
Health
Contact Information for Business Card
Tessa Ravenna Holloway
Life and Wellness Coach
tessa@coachtrh.com
www.brightpathwell.com
443-781-6392
Health is not an event it's a lifestyle (tag line or if you have a better tag line)

```html
<!DOCTYPE html>
<html lang="en">
<head>
<meta charset="utf-8">
<title>Tessa Ravenna Holloway – Business Card</title>
<link rel="stylesheet" href="https://fonts.googleapis.com/css2?family=Source+Sans+3:wght@300;400&display=swap">
<style>
  :root {
    --backdrop: #c6c7ca;
    --card: #ffffff;
    --ink: #3b3b3d;
    --gold: #b38b2e;
    --band: #3d3d3f;
    --on-band: #ffffff;
  }
  * { margin: 0; padding: 0; box-sizing: border-box; }
  html, body {
    width: 1200px;
    height: 960px;
    overflow: hidden;
    background: var(--backdrop);
    font-family: "Source Sans 3", sans-serif;
  }
  .business-card {
    position: absolute;
    left: 75px;
    top: 180px;
    width: 1050px;
    height: 600px;
    background: var(--card);
  }
  .card-header {
    position: absolute;
    top: 86px;
    left: 0;
    width: 100%;
    text-align: center;
  }
  .holder-name {
    font-size: 33px;
    font-weight: 400;
    color: var(--ink);
    line-height: 1;
  }
  .holder-title {
    margin-top: 2px;
    font-size: 28px;
    font-weight: 400;
    color: var(--gold);
    line-height: 1.1;
  }
  .brand-mark {
    position: absolute;
    top: 210px;
    left: 0;
    width: 100%;
    text-align: center;
    font-size: 130px;
    font-weight: 300;
    letter-spacing: 4px;
    color: var(--gold);
    line-height: 1;
  }
  .tagline {
    position: absolute;
    top: 346px;
    left: 0;
    width: 100%;
    text-align: center;
    font-size: 28px;
    font-weight: 400;
    color: var(--ink);
  }
  .contact-strip {
    position: absolute;
    left: 0;
    top: 540px;
    width: 100%;
    height: 44px;
  }
  .contact-rule {
    position: absolute;
    left: 0;
    bottom: 3px;
    width: 100%;
    height: 3px;
    background: var(--band);
  }
  .phone-tab {
    position: absolute;
    left: 345px;
    top: 9px;
    width: 360px;
    height: 33px;
  }
  .contact-item {
    position: absolute;
    font-size: 27px;
    font-weight: 400;
    color: var(--ink);
    line-height: 1;
  }
  .contact-email { left: 34px; top: 6px; }
  .contact-web { right: 36px; top: 6px; }
  .contact-phone {
    left: 345px;
    width: 360px;
    top: 15px;
    text-align: center;
    color: var(--on-band);
    font-size: 26px;
  }
</style>
</head>
<body>
  <main class="business-card">
    <header class="card-header">
      <h1 class="holder-name">Tessa Ravenna Holloway</h1>
      <p class="holder-title">Life and Wellness Coach</p>
    </header>

    <div class="brand-mark">TRH</div>

    <p class="tagline">Health is not an event it's a lifestyle</p>

    <footer class="contact-strip">
      <div class="contact-rule"></div>
      <svg class="phone-tab" viewBox="0 0 360 33" aria-hidden="true">
        <path d="M0 33 L24 8 Q32 0 44 0 H312 Q330 0 340 12 L360 33 Z" fill="var(--band)"/>
      </svg>
      <span class="contact-item contact-email">tessa@coachtrh.com</span>
      <span class="contact-item contact-phone">443-781-6392</span>
      <span class="contact-item contact-web">www.brightpathwell.com</span>
    </footer>
  </main>
</body>
</html>
```